uk plumbing and heating van wrap design

my company welden gas requires a cutting edge modern design that can be applied to our vehicles that makes them stand out from the crowd. we are a plumbing/heating company from the uk, we service/repair/install all sorts of heating and plumbing systems in our customers homes. we want our vehicles to become a familiar sight due to their branding. We want a very professional, modern and contemporary design that’s not too loud or in your face but that when you see it you know it’s us.

Colors
0592cd
33a6d7
ec1f27
f04a50
ffffff

Requirements
Must have
• 1. Chevron design on back doors in yellow/red (see examples)
• 2. A half wrap design only, that covers from the middle to the back of the vehicle
• 3. My logo on both sides of the van, back doors and bonnet
• 4. Incorporate the colours red/blue into the design (mainly red)
• 5. The design is shown as an example on the correct vehicle (Harnow tessamo 2016 model)
Nice to have
• A design similar to the ones I’ve provided as examples but with our own twist on them. Something abstract and modern.
Should not have
• 1. A full wrap design
• 2. Logo running diagonally on side of vehicle
• 3. Logo must stay intact as provided and not split up eg separating the emblem and wording from the logo and repositioning them.

```html
<!DOCTYPE html>
<html lang="en">
<head>
<meta charset="utf-8">
<title>Welden Gas – Van Wrap Design</title>
<link href="https://fonts.googleapis.com/css2?family=Michroma&family=Roboto+Condensed:wght@700&family=Roboto:wght@700&display=swap" rel="stylesheet">
<style>
  :root {
    --brand-blue: #0592cd;
    --brand-blue-light: #33a6d7;
    --brand-red: #ec1f27;
    --brand-red-light: #f04a50;
    --white: #ffffff;
    --wrap-black: #0d0d0f;
    --chevron-yellow: #e3ec12;
    --trim-orange: #e8641c;
    --phone-grey: #d9d9d9;
    --canvas-bg: #f4f4f4;
  }
  * { margin: 0; padding: 0; box-sizing: border-box; }
  html, body { width: 1200px; height: 1200px; overflow: hidden; background: var(--canvas-bg); }
  .canvas { position: relative; width: 1200px; height: 1200px; }

  .side-view { position: absolute; left: 60px; top: 80px; width: 1080px; height: 500px; }
  .brand-name { font-family: "Michroma", sans-serif; fill: var(--white); }
  .brand-tagline { font-family: "Michroma", sans-serif; fill: var(--white); }
  .web-address { font-family: "Roboto", sans-serif; font-weight: 700; fill: #10202a; }
  .phone-number { font-family: "Roboto Condensed", sans-serif; font-weight: 700; fill: var(--phone-grey); letter-spacing: 2px; }

  .rear-doors {
    position: absolute; left: 140px; top: 690px; width: 400px; height: 440px;
    background: var(--wrap-black); border-radius: 26px 26px 10px 10px; overflow: hidden;
  }
  .rear-logo { height: 160px; display: flex; align-items: center; justify-content: center; gap: 16px; }
  .chevrons { position: absolute; left: 0; right: 0; bottom: 0; height: 280px; display: flex; }
  .chevron-half { flex: 1; }
  .chevron-half.left {
    background: repeating-linear-gradient(-45deg, var(--brand-red) 0 36px, var(--chevron-yellow) 36px 72px);
  }
  .chevron-half.right {
    background: repeating-linear-gradient(45deg, var(--brand-red) 0 36px, var(--chevron-yellow) 36px 72px);
  }
  .door-split { position: absolute; left: 199px; top: 160px; bottom: 0; width: 2px; background: rgba(0,0,0,.45); }

  .bonnet {
    position: absolute; left: 640px; top: 690px; width: 440px; height: 440px;
    background: var(--wrap-black); border-radius: 90px 90px 20px 20px;
    display: flex; align-items: center; justify-content: center;
  }
  .bonnet-logo { display: flex; align-items: center; gap: 12px; margin-top: -60px; }

  .logo-dot { border-radius: 50%; background: var(--brand-blue-light); flex: none; }
  .logo-words { display: flex; flex-direction: column; }
  .logo-name { font-family: "Michroma", sans-serif; color: var(--white); line-height: 1; }
  .logo-tag { font-family: "Michroma", sans-serif; color: var(--white); line-height: 1; margin-top: 6px; white-space: nowrap; }

  .rear-logo .logo-dot { width: 58px; height: 58px; }
  .rear-logo .logo-name { font-size: 46px; }
  .rear-logo .logo-tag { font-size: 11px; letter-spacing: .5px; }
  .bonnet-logo .logo-dot { width: 40px; height: 40px; }
  .bonnet-logo .logo-name { font-size: 34px; }
  .bonnet-logo .logo-tag { font-size: 8px; letter-spacing: .5px; }
</style>
</head>
<body>
<main class="canvas">

  <svg class="side-view" viewBox="0 0 1080 500" aria-label="Side wrap layout">
    <defs>
      <clipPath id="body-clip">
        <path d="M40 30 H780 Q880 30 950 150 L1040 270 Q1062 305 1062 345 V450 Q1062 480 1032 480 H40 Q18 480 18 452 V58 Q18 30 40 30 Z"/>
      </clipPath>
    </defs>
    <path class="van-body" fill="var(--wrap-black)" d="M40 30 H780 Q880 30 950 150 L1040 270 Q1062 305 1062 345 V450 Q1062 480 1032 480 H40 Q18 480 18 452 V58 Q18 30 40 30 Z"/>
    <g clip-path="url(#body-clip)">
      <path class="stripe-blue" fill="var(--brand-blue-light)" d="M0 270 H520 Q560 270 585 300 L740 480 H700 L560 325 Q545 305 515 305 H0 Z"/>
      <path class="stripe-red" fill="var(--brand-red)" d="M0 322 H500 Q535 322 555 345 L680 480 H0 Z"/>
      <path class="stripe-orange" fill="var(--trim-orange)" d="M0 462 H664 L681 480 H0 Z"/>
    </g>
    <circle class="logo-mark" cx="150" cy="150" r="58" fill="var(--brand-blue-light)"/>
    <text class="brand-name" x="232" y="186" font-size="92">WELDEN</text>
    <text class="brand-tagline" x="236" y="236" font-size="22" letter-spacing="1">GAS | HEATING | PLUMBING</text>
    <text class="web-address" x="150" y="297" font-size="21">www.weldengasservices.co.uk</text>
    <text class="phone-number" x="680" y="312" font-size="38">121 555 0194</text>
  </svg>

  <section class="rear-doors" aria-label="Rear doors wrap">
    <div class="rear-logo">
      <span class="logo-dot"></span>
      <div class="logo-words">
        <span class="logo-name">WELDEN</span>
        <span class="logo-tag">GAS | HEATING | PLUMBING</span>
      </div>
    </div>
    <div class="chevrons">
      <div class="chevron-half left"></div>
      <div class="chevron-half right"></div>
    </div>
    <div class="door-split"></div>
  </section>

  <section class="bonnet" aria-label="Bonnet wrap">
    <div class="bonnet-logo">
      <span class="logo-dot"></span>
      <div class="logo-words">
        <span class="logo-name">WELDEN</span>
        <span class="logo-tag">GAS | HEATING | PLUMBING</span>
      </div>
    </div>
  </section>

</main>
</body>
</html>
```